Brimble Diecast Torvel Collectables Website

looking for a vibrant web site marketplace built for diecast car enthusiasts to buy, sell, and trade with ease. Whether you're looking to showcase your own collection or discover rare and exciting models, our site makes the process simple and enjoyable. Clients can browse a curated inventory of high‑quality diecast cars, connect with fellow collectors, and find the perfect pieces to expand their collection. With a smooth user experience and a community-driven spirit, we’re the go‑to destination for anyone passionate about diecast cars.

Target Market(s)

diecast collectors

Industry/Entity Type

Diecast Collectables

Coding

Coded - Design and coding required

Number of Pages Required

3 page

Font styles to use
Sans Serif

Colors
EE7325
F08F49
F5BC92
FAE3D3
FDF4ED

Requirements
Must have
• Cool look and feel. Woo commerce page to post and sell my inventory
Nice to have
• page for users to post their cars or looking for trades.
Should not have
• look cheap

```html
<!DOCTYPE html>
<html lang="en">
<head>
<meta charset="utf-8">
<title>Brimble Diecast — Shop</title>
<link href="https://fonts.googleapis.com/css2?family=Inter:wght@400;500;600;700&family=Plus+Jakarta+Sans:wght@500;600;700&display=swap" rel="stylesheet">
<style>
:root{
  --bg:#161616;
  --nav:#131313;
  --panel:#1f1f1f;
  --field:#0f0f0f;
  --ink:#f2f2f2;
  --muted:#b9b9b9;
  --dim:#8a8a8a;
  --orange:#EE7325;
  --orange-2:#F08F49;
  --peach:#F5BC92;
  --cream:#FAE3D3;
  --shell:#FDF4ED;
}
*{box-sizing:border-box;margin:0;padding:0}
html,body{width:876px;height:1200px;overflow:hidden;background:var(--bg);color:var(--ink);font-family:"Inter",sans-serif}
.page{position:relative;width:876px;height:1200px}
.abs{position:absolute}
.display{font-family:"Plus Jakarta Sans","Inter",sans-serif}

.nav{left:0;top:0;width:876px;height:48px;background:var(--nav);display:flex;align-items:center;padding:0 29px}
.burger{width:12px;height:9px;display:flex;flex-direction:column;justify-content:space-between;margin-right:14px}
.burger span{height:1.5px;background:var(--ink);display:block}
.logo{font-family:"Plus Jakarta Sans",sans-serif;font-weight:700;color:var(--orange);font-size:14px;letter-spacing:-.3px}
.menu{position:absolute;left:389px;top:0;height:48px;display:flex;gap:20px;align-items:center}
.menu a{font-size:7.5px;letter-spacing:1.2px;font-weight:500;color:var(--ink);text-decoration:none}
.menu a.active{color:var(--orange)}
.cart{position:absolute;left:819px;top:19px}

.hero-title{left:29px;top:56px;font-size:46px;font-weight:600;letter-spacing:-1.6px;line-height:1}
.hero-title em{font-style:normal;color:var(--orange)}
.hero-copy{left:29px;top:118px;width:410px;font-size:11.3px;line-height:18px;color:var(--muted)}
.tabs{left:647px;top:142px;width:200px;height:28px;background:var(--panel);border-radius:5px;display:flex;align-items:center;padding:0 4px}
.tab{font-size:6.2px;letter-spacing:.9px;font-weight:600;color:var(--ink);height:19px;display:flex;align-items:center;justify-content:center;flex:1}
.tab.on{background:var(--orange);border-radius:3px;flex:0 0 64px}

.filters{left:29px;top:207px;display:flex;gap:8px}
.chip{height:24px;padding:0 10px;background:var(--panel);border-radius:4px;font-size:8.5px;display:flex;align-items:center;gap:5px}
.search{left:537px;top:207px;width:156px;height:24px;background:var(--field);border-radius:4px;display:flex;align-items:center;padding:0 8px;gap:7px;font-size:8.5px;color:var(--dim)}
.sort{left:703px;top:207px;width:144px;height:24px;border-left:1px solid #2a2a2a;display:flex;align-items:center;justify-content:space-between;padding:0 6px 0 17px;font-size:8.5px;letter-spacing:1.4px;font-weight:600}

.card{top:285px;width:190px}
.photo{width:190px;height:142px;border-radius:8px;position:relative}
.tag{position:absolute;left:10px;top:10px;height:13px;padding:0 7px;border-radius:7px;font-size:6px;letter-spacing:.8px;font-weight:600;display:flex;align-items:center}
.tag.hot{background:var(--orange);color:#1b1b1b}
.tag.soft{background:var(--cream);color:#6a3a1a}
.meta{display:flex;justify-content:space-between;align-items:flex-start;padding:0 2px;margin-top:15px}
.maker{font-size:6px;letter-spacing:.9px;color:var(--muted);font-weight:500;margin-top:2px}
.price{font-size:12.5px;color:var(--orange-2);font-weight:600}
.name{font-size:12.3px;font-weight:600;line-height:15px;padding:0 2px;margin-top:5px;height:30px}
.name.one{height:15px;white-space:nowrap}
.specs{margin:8px 2px 0;background:var(--panel);border-radius:4px;height:35px;display:flex;padding:0 7px;align-items:center}
.spec{flex:1}
.spec small{display:block;font-size:5.3px;letter-spacing:.6px;color:var(--dim)}
.spec b{display:block;font-size:7.5px;font-weight:500;margin-top:3px}
.buy{margin:15px 2px 0;height:29px;border-radius:3px;background:linear-gradient(90deg,var(--orange),var(--peach));display:flex;align-items:center;justify-content:center;font-size:8px;letter-spacing:2.2px;font-weight:600;color:#1a1a1a}

.spot{left:29px;top:647px;width:468px;height:302px;border-radius:10px;overflow:hidden;background:radial-gradient(ellipse at 55% 45%,#7a7a7a 0%,#3c3c3c 40%,#1a1a1a 75%),#1a1a1a}
.spot .glow{position:absolute;left:30px;top:0;width:70px;height:190px;background:linear-gradient(180deg,#d18a16,#6b4a10 60%,transparent);filter:blur(8px);opacity:.8}
.spot .shade{position:absolute;inset:0;background:linear-gradient(180deg,transparent 45%,rgba(15,15,15,.9) 100%)}
.spot-label{position:absolute;left:20px;top:200px;height:13px;padding:0 7px;border-radius:7px;background:#3a2516;color:var(--orange);font-size:6px;letter-spacing:.9px;font-weight:600;display:flex;align-items:center}
.spot-title{position:absolute;left:20px;top:221px;font-size:23px;font-weight:700;letter-spacing:-.6px}
.spot-copy{position:absolute;left:20px;top:255px;font-size:9.8px;line-height:14.5px;color:#d5d5d5}
.join{left:517px;top:647px;width:330px;height:302px;border-radius:10px;background:var(--panel)}
.join h2{position:absolute;left:25px;top:74px;font-size:15.5px;font-weight:600}
.join p{position:absolute;left:25px;top:107px;width:290px;font-size:9.8px;line-height:16px;color:var(--muted)}
.email{position:absolute;left:25px;top:157px;width:281px;height:33px;background:var(--field);border-radius:4px;font-size:9.8px;color:var(--dim);display:flex;align-items:center;padding-left:15px}
.subscribe{position:absolute;left:25px;top:200px;width:281px;height:29px;background:#2f2f2f;border-radius:4px;font-size:7.5px;letter-spacing:1.2px;font-weight:600;color:var(--orange-2);display:flex;align-items:center;justify-content:center}

.footer{left:0;top:1006px;width:876px;height:194px;background:#121212}
.f-logo{position:absolute;left:27px;top:51px;font-size:14.5px}
.f-about{position:absolute;left:27px;top:82px;width:200px;font-size:8.6px;line-height:14px;color:#cfcfcf}
.f-icons{position:absolute;left:27px;top:125px;display:flex;gap:10px}
.f-icon{width:24px;height:24px;border-radius:5px;background:#262626;display:flex;align-items:center;justify-content:center}
.f-col{position:absolute;top:52px}
.f-col h4{font-size:6.2px;letter-spacing:1px;font-weight:700;color:var(--orange-2);margin-bottom:13px}
.f-col a{display:block;font-size:8.7px;color:#d5d5d5;text-decoration:none;margin-bottom:10.5px}
</style>
</head>
<body>
<div class="page">

  <header class="nav abs">
    <div class="burger"><span></span><span></span><span></span></div>
    <div class="logo">Brimble Diecast</div>
    <nav class="menu">
      <a href="#">HOME</a><a href="#" class="active">SHOP</a><a href="#">EXCHANGE</a><a href="#">ACCOUNT</a>
    </nav>
    <svg class="cart" width="15" height="14" viewBox="0 0 15 14" fill="none" stroke="#eee" stroke-width="1.3">
      <path d="M1 2h2l2 7h6.5l1.6-5H4"/><circle cx="6" cy="12" r="1"/><circle cx="11" cy="12" r="1"/>
      <circle cx="13" cy="1.8" r="1.6" fill="#EE7325" stroke="none"/>
    </svg>
  </header>

  <h1 class="hero-title abs display">Curated <em>Excellence</em></h1>
  <p class="hero-copy abs">Discover a master-grade collection of limited edition diecast models. From vintage muscle to modern hypercars, precision engineering meets collector passion.</p>

  <div class="tabs abs">
    <div class="tab on">ALL MODELS</div><div class="tab">PRE-ORDERS</div><div class="tab">VAULT</div>
  </div>

  <div class="filters abs">
    <div class="chip">Brand <svg width="6" height="4" viewBox="0 0 6 4"><path d="M.5.5 3 3 5.5.5" fill="none" stroke="#eee"/></svg></div>
    <div class="chip">Scale <svg width="6" height="4" viewBox="0 0 6 4"><path d="M.5.5 3 3 5.5.5" fill="none" stroke="#eee"/></svg></div>
    <div class="chip">Condition <svg width="6" height="4" viewBox="0 0 6 4"><path d="M.5.5 3 3 5.5.5" fill="none" stroke="#eee"/></svg></div>
  </div>
  <div class="search abs">
    <svg width="9" height="9" viewBox="0 0 9 9" fill="none" stroke="#ddd" stroke-width="1.3"><circle cx="3.6" cy="3.6" r="2.8"/><path d="M5.7 5.7 8.5 8.5"/></svg>
    Search collection...
  </div>
  <div class="sort abs">LATEST <svg width="6" height="4" viewBox="0 0 6 4"><path d="M.5.5 3 3 5.5.5" fill="none" stroke="#bbb"/></svg></div>

  <article class="card abs" style="left:29px">
    <div class="photo" role="img" aria-label="Red 1967 muscle car model on white backdrop" style="background:linear-gradient(180deg,#fafafa,#e9e9e9)"><span class="tag hot">RARE FINDING</span></div>
    <div class="meta"><span class="maker">CALDER MOTORWORKS • 1:18</span><span class="price">$289.00</span></div>
    <h3 class="name display">1967 Calder Stormline – Nightmist Blue</h3>
    <div class="specs"><div class="spec"><small>CONDITION</small><b>Mint in Box</b></div><div class="spec"><small>YEAR</small><b>2023 Release</b></div></div>
    <div class="buy">ADD TO CART</div>
  </article>

  <article class="card abs" style="left:238px">
    <div class="photo" role="img" aria-label="Orange sports coupe model on grey gradient backdrop" style="background:linear-gradient(180deg,#3e4650,#9aa0a6 55%,#f0f0f0)"></div>
    <div class="meta"><span class="maker">VELTMANN DESIGN • 1:43</span><span class="price">$115.00</span></div>
    <h3 class="name one display">Veltmann Tempo – Lava Orange</h3>
    <div class="specs"><div class="spec"><small>CONDITION</small><b>New Release</b></div><div class="spec"><small>YEAR</small><b>2024 Edition</b></div></div>
    <div class="buy" style="margin-top:31px">ADD TO CART</div>
  </article>

  <article class="card abs" style="left:447px">
    <div class="photo" role="img" aria-label="Blue hypercar model on a black display base" style="background:linear-gradient(180deg,#f6f6f6,#dcdcdc 60%,#2a2c30)"><span class="tag soft">LOW STOCK</span></div>
    <div class="meta"><span class="maker">MODELFORGE • 1:18</span><span class="price">$340.00</span></div>
    <h3 class="name display">Raveno Ardente XR – Blu Marino</h3>
    <div class="specs"><div class="spec"><small>CONDITION</small><b>A+ Collector Grade</b></div><div class="spec"><small>YEAR</small><b>Limited 500 pcs</b></div></div>
    <div class="buy">ADD TO CART</div>
  </article>

  <article class="card abs" style="left:657px">
    <div class="photo" role="img" aria-label="Silver 1971 classic coupe model on dark backdrop" style="background:radial-gradient(ellipse at 50% 55%,#8a8a8a,#3a3a3a 55%,#1e1e1e)"></div>
    <div class="meta"><span class="maker">LUNARO • 1:18</span><span class="price">$185.00</span></div>
    <h3 class="name display">1971 Kessler Grand Coupé – Silver</h3>
    <div class="specs"><div class="spec"><small>CONDITION</small><b>Original Packaging</b></div><div class="spec"><small>YEAR</small><b>Historical Series</b></div></div>
    <div class="buy">ADD TO CART</div>
  </article>

  <section class="spot abs" role="img" aria-label="Close-up of a detailed miniature V-twin engine with warm amber light behind">
    <div class="glow"></div><div class="shade"></div>
    <span class="spot-label">COLLECTOR'S SPOTLIGHT</span>
    <h2 class="spot-title display">The Detail Workshop</h2>
    <p class="spot-copy">Every engine bay, every dashboard, every stitch.<br>Explore models with unparalleled realism.</p>
  </section>

  <section class="join abs">
    <h2 class="display">Join the Inner Circle</h2>
    <p>Be the first to receive notifications for private auctions, limited production runs, and exclusive "Vault" access.</p>
    <div class="email">Your email address</div>
    <div class="subscribe">SUBSCRIBE NOW</div>
  </section>

  <footer class="footer abs">
    <div class="logo f-logo">Brimble Diecast</div>
    <p class="f-about">The definitive destination for high-end diecast enthusiasts. Precision in every scale.</p>
    <div class="f-icons">
      <div class="f-icon"><svg width="11" height="11" viewBox="0 0 12 12" fill="none" stroke="#ddd" stroke-width="1.1"><circle cx="6" cy="6" r="5"/><path d="M1 6h10M6 1c2 2 2 8 0 10M6 1c-2 2-2 8 0 10"/></svg></div>
      <div class="f-icon"><svg width="11" height="11" viewBox="0 0 12 12" fill="none" stroke="#ddd" stroke-width="1.1"><circle cx="9" cy="2.5" r="1.5"/><circle cx="3" cy="6" r="1.5"/><circle cx="9" cy="9.5" r="1.5"/><path d="M4.3 5.2 7.7 3.3M4.3 6.8l3.4 1.9"/></svg></div>
    </div>
    <div class="f-col" style="left:261px"><h4>SHOP</h4><a href="#">1:18 Scale</a><a href="#">1:43 Scale</a><a href="#">New Arrivals</a><a href="#">Bestsellers</a></div>
    <div class="f-col" style="left:491px"><h4>SUPPORT</h4><a href="#">Shipping Policy</a><a href="#">Return Portal</a><a href="#">Condition Guide</a><a href="#">FAQ</a></div>
    <div class="f-col" style="left:721px"><h4>LEGAL</h4><a href="#">Privacy Policy</a><a href="#">Terms of Service</a><a href="#">Cookie Settings</a></div>
  </footer>

</div>
</body>
</html>
```